Website/Logo redesign: FieldKinship.com

We need a web design for a sports social network.
We have already built the web-site but are unhappy with the current design.
We like colours that evoke outdoors, eg sky blue and grass green.
Please see how it currently looks:
http://www.fieldkinship.example/4b1a9c3e7d2f5a8b0c6e1f3a9d7b2c5e/
We are happy for everything to change, including logo, icons etc or for you to keep anything you think will work with your new design.
Reason: We have not yet found the design we are happy with so will be providing more feedback and extending the deadine.
We have increased the budget and also agreed to pay a second place award.
I will be giving existing and any new designs feedback daily.
Target Market(s)
Our target audience are mainly young sports players, but also older ones too.
Industry/Entity Type
Social
Look and feel

```html
<!DOCTYPE html>
<html lang="en">
<head>
<meta charset="utf-8">
<title>Field Kinship</title>
<link rel="stylesheet" href="https://fonts.googleapis.com/css2?family=Arimo:wght@400;700&family=Oswald:wght@400;500;600&family=Tinos&family=Noto+Serif:ital@0;1&display=swap">
<style>
:root{
  --black:#000;
  --white:#fff;
  --nav-top:#9dd04c;
  --nav-bottom:#74ad2c;
  --nav-active:#3f5b22;
  --nav-line:#5f8f25;
  --grass-light:#b6d98a;
  --grass-mid:#7fb53e;
  --grass-dark:#4d7f22;
  --panel:rgba(243,247,238,0.78);
  --panel-edge:rgba(255,255,255,0.6);
  --ink:#4a4a4a;
  --muted:#8a8a8a;
  --faint:#b4b4b4;
  --team-green:#2f9a2f;
  --team-red:#e0532b;
  --badge:#d8262d;
  --button-green:#7dbb2c;
  --line:#cfd3c9;
}
*{box-sizing:border-box;margin:0;padding:0}
html,body{width:1050px;height:1200px;overflow:hidden;background:var(--black)}
body{font-family:"Arimo",Arial,sans-serif;color:var(--ink);position:relative}
.abs{position:absolute}
.top-bar{left:0;top:0;width:1050px;height:47px;background:var(--black);color:var(--white);font-family:"Tinos",serif;font-size:24px}
.top-bar .welcome{left:22px;top:10px}
.top-bar .login{left:942px;top:10px}
.main-nav{left:0;top:47px;width:1050px;height:82px;background:linear-gradient(var(--nav-top),var(--nav-bottom))}
.brand{left:50px;top:13px;display:flex;align-items:center;gap:8px}
.brand-square{width:52px;height:52px;background:var(--white)}
.brand-name{font-family:"Oswald",sans-serif;font-weight:400;font-size:25px;color:var(--white);letter-spacing:.5px}
.nav-item{top:0;width:73px;height:82px;border-left:1px solid var(--nav-line);color:#3c5a1c;font-family:"Oswald",sans-serif;font-size:11px;text-align:center}
.nav-item svg{position:absolute;left:24px;top:16px}
.nav-item span{position:absolute;left:0;right:0;top:52px}
.nav-item.active{background:var(--nav-active);color:var(--white)}
.badge{width:18px;height:18px;border-radius:50%;background:var(--badge);color:var(--white);font-size:11px;font-weight:700;text-align:center;line-height:18px;top:6px;left:51px}
.signup{left:952px;top:0;width:98px;height:82px;border-left:1px solid var(--nav-line);color:var(--white);font-family:"Tinos",serif;font-size:22px;text-align:center;line-height:25px;padding-top:6px}
.grass{left:0;top:129px;width:1050px;height:1030px;background:radial-gradient(ellipse at 50% 40%,var(--grass-light),var(--grass-mid) 55%,var(--grass-dark))}
.bottom-bar{left:0;top:1159px;width:1050px;height:41px;background:var(--black)}
.panel{background:var(--panel);border:1px solid var(--panel-edge)}
.card{background:rgba(255,255,255,0.25);border:1px solid rgba(190,195,185,0.7);border-radius:3px}
.photo{background:linear-gradient(135deg,#d8b48a,#9c6d4a)}
.pill{border:1px solid #bfc3ba;border-radius:12px;background:linear-gradient(#fbfbf8,#e4e6df);font-size:10px;text-align:center;color:var(--ink)}
.label{font-family:"Oswald",sans-serif;font-size:12px;font-weight:500;color:#3e3e3e;letter-spacing:.5px}
.label.faded{color:#9aa094}
.small{font-size:10px;line-height:15px}
.name{font-weight:700;font-size:10px;color:#444}
.green{color:var(--team-green);font-weight:700}
.red{color:var(--team-red);font-weight:700}
.time{font-size:10px;color:var(--muted);text-align:right}
.rule{height:1px;background:var(--line)}
.hatch{height:6px;background:repeating-linear-gradient(135deg,#d4d7cf 0 1px,transparent 1px 4px)}
.team-row{left:120px;width:222px;height:42px;border:1px solid rgba(200,205,195,0.7);border-top:none;font-family:"Oswald",sans-serif;font-size:13px;color:var(--faint);padding:11px 0 0 38px}
.team-row svg{position:absolute;left:10px;top:13px}
.quote{font-family:"Noto Serif",serif;font-size:12.5px;line-height:21px;color:#6a6a6a}
.icon-box{width:35px;height:36px;border:1px solid #c4c8be;background:rgba(255,255,255,0.5);border-radius:2px}
.icon-box svg{position:absolute;left:6px;top:6px}
.mini{width:20px;height:20px;border:1px solid #bfc3ba;border-radius:50%;background:#f5f6f2}
.mini svg{position:absolute;left:3px;top:3px}
.league-table{left:765px;top:523px;width:248px;height:260px}
.league-row{left:780px;width:220px;height:16px;font-size:11px;color:#555;font-weight:700}
.league-row .pos{position:absolute;left:16px}
.league-row .team{position:absolute;left:44px}
.league-row .played{position:absolute;left:152px;width:24px;text-align:center}
.league-row .pts{position:absolute;left:186px;width:26px;text-align:right}
</style>
</head>
<body>

<header>
  <div class="abs top-bar">
    <div class="abs welcome">WELCOME TO THE FIELD KINSHIP'S OFFICIAL WEBSITE.</div>
    <div class="abs login">LOG IN</div>
  </div>
  <nav class="abs main-nav">
    <div class="abs brand"><div class="brand-square"></div><div class="brand-name">FIELD KINSHIP</div></div>

    <div class="abs nav-item active" style="left:439px">
      <svg width="24" height="28" viewBox="0 0 24 28"><path d="M5 2v24" stroke="#fff" stroke-width="2.5"/><path d="M6 3h14l-3 6 3 6H6z" fill="#fff"/></svg>
      <span>HEADLINES</span>
    </div>
    <div class="abs badge" style="left:490px">2</div>
    <div class="abs nav-item" style="left:512px">
      <svg width="26" height="26" viewBox="0 0 26 26" fill="none" stroke="#3c5a1c" stroke-width="1.6"><path d="M2 2v22h22"/><path d="M5 19l5-6 4 3 8-11"/></svg>
      <span>MY STATS</span>
    </div>
    <div class="abs nav-item" style="left:585px">
      <svg width="24" height="28" viewBox="0 0 24 28"><path d="M12 2c2 6 9 9 9 16a9 9 0 0 1-18 0c0-4 2-6 4-8 0 3 1 5 3 5-1-5 0-9 2-13z" fill="#3c5a1c"/></svg>
      <span>CHLLNGRS</span>
    </div>
    <div class="abs badge" style="left:636px">1</div>
    <div class="abs nav-item" style="left:659px">
      <svg width="24" height="26" viewBox="0 0 24 26" fill="none" stroke="#3c5a1c" stroke-width="1.6"><rect x="2" y="4" width="20" height="20"/><path d="M2 10h20M7 1v6M17 1v6M7 14h2M11 14h2M15 14h2M7 18h2M11 18h2M15 18h2"/></svg>
      <span>FIXTURES</span>
    </div>
    <div class="abs nav-item" style="left:732px">
      <svg width="28" height="24" viewBox="0 0 28 24" fill="#3c5a1c"><circle cx="8" cy="7" r="4"/><circle cx="20" cy="7" r="4"/><path d="M0 22c0-6 4-9 8-9s8 3 8 9zM12 22c0-6 4-9 8-9s8 3 8 9z"/></svg>
      <span>TEAMS</span>
    </div>
    <div class="abs nav-item" style="left:805px">
      <svg width="24" height="26" viewBox="0 0 24 26" fill="none" stroke="#3c5a1c" stroke-width="1.6"><rect x="3" y="2" width="18" height="22"/><path d="M3 8h18M3 13h18M3 18h18M9 2v22"/></svg>
      <span>LEAGUES</span>
    </div>
    <div class="abs nav-item" style="left:879px">
      <svg width="26" height="26" viewBox="0 0 26 26" fill="none" stroke="#3c5a1c" stroke-width="2.4" stroke-linecap="round"><path d="M4 22l12-12M16 4a5 5 0 0 0 6 6M4 4l18 18"/></svg>
      <span>TOOLS</span>
    </div>
    <div class="abs signup">OR<br>SIGN UP</div>
  </nav>
</header>

<div class="abs grass" role="img" aria-label="Close-up photograph of green grass blades as page background"></div>

<!-- Left column -->
<aside class="abs panel" style="left:20px;top:154px;width:324px;height:977px"></aside>

<section class="abs card profile-card" style="left:120px;top:155px;width:196px;height:133px">
  <div class="abs photo" role="img" aria-label="Profile photo of Owen Marsh" style="left:10px;top:10px;width:50px;height:54px"></div>
  <div class="abs" style="left:72px;top:14px;font-size:13px;font-weight:700;color:#444">Owen Marsh</div>
  <div class="abs pill" style="left:72px;top:35px;width:72px;height:22px;line-height:20px">Edit profile</div>
  <div class="abs rule" style="left:0;top:75px;width:194px"></div>
  <div class="abs" style="left:10px;top:84px;font-size:16px;color:#555">24</div>
  <div class="abs" style="left:79px;top:84px;font-size:16px;color:#555">3</div>
  <div class="abs" style="left:146px;top:84px;font-size:16px;color:#555">7</div>
  <div class="abs" style="left:10px;top:107px;font-size:10px;color:var(--muted)">Played</div>
  <div class="abs" style="left:79px;top:107px;font-size:10px;color:var(--muted)">Teams</div>
  <div class="abs" style="left:146px;top:107px;font-size:10px;color:var(--muted)">Awards</div>
</section>

<div class="abs card create-fixture" style="left:120px;top:317px;width:196px;height:42px">
  <svg class="abs" style="left:12px;top:14px" width="13" height="13" viewBox="0 0 13 13"><path d="M6.5 0v13M0 6.5h13" stroke="#555" stroke-width="2"/></svg>
  <div class="abs label" style="left:38px;top:12px">CREATE NEW FIXTURE</div>
</div>

<div class="abs card" style="left:120px;top:416px;width:222px;height:42px;border-radius:0">
  <div class="abs label" style="left:40px;top:12px">ALL TEAMS</div>
</div>
<div class="abs team-row" style="top:458px"><svg width="14" height="14" viewBox="0 0 14 14"><circle cx="7" cy="7" r="6" fill="none" stroke="#999"/><path d="M7 4l3 2-1 3H5L4 6z" fill="#999"/></svg>U15 FOOTBALL TEAM B</div>
<div class="abs team-row" style="top:500px"><svg width="14" height="14" viewBox="0 0 14 14"><circle cx="7" cy="7" r="6" fill="none" stroke="#999"/><path d="M7 4l3 2-1 3H5L4 6z" fill="#999"/></svg>GALATIANS HOUSE</div>
<div class="abs team-row" style="top:542px"><svg width="14" height="14" viewBox="0 0 14 14"><circle cx="7" cy="7" r="6" fill="none" stroke="#999"/><path d="M7 4l3 2-1 3H5L4 6z" fill="#999"/></svg>U15 RUGBY TEAM A</div>

<div class="abs label" style="left:132px;top:637px">QUOTE OF THE DAY</div>
<p class="abs quote" style="left:132px;top:676px;width:200px">Champions aren’t made in the gyms. Champions are made from something they have deep inside them — a desire, a dream, a vision.</p>
<div class="abs quote" style="left:132px;top:782px;width:180px;text-align:right;font-style:italic">— Marcus Reed</div>

<!-- Centre column -->
<main class="abs panel" style="left:344px;top:154px;width:402px;height:877px"></main>

<div class="abs label" style="left:364px;top:171px;font-size:11px">NEXT FIXTURE</div>
<div class="abs hatch" style="left:460px;top:176px;width:262px"></div>

<div class="abs icon-box" style="left:365px;top:204px"><svg width="22" height="22" viewBox="0 0 22 22"><circle cx="11" cy="11" r="10" fill="#fff" stroke="#333" stroke-width="1.5"/><path d="M11 6l4 3-1.5 4.5h-5L7 9z" fill="#333"/></svg></div>
<div class="abs mini" style="left:414px;top:212px"><svg width="12" height="12" viewBox="0 0 12 12"><path d="M1 11V5h3v6M4.5 11V2h3v9M8 11V6h3v5" fill="none" stroke="#777"/></svg></div>
<div class="abs small" style="left:449px;top:208px"><span class="green">U15 Football Team</span> vs <span class="red">Colossians House</span></div>
<div class="abs small" style="left:449px;top:223px;color:#666">Sunday, 29th July, 1 PM</div>
<div class="abs" style="left:449px;top:251px;font-size:10px;font-weight:700;color:#444">RSVP:</div>
<div class="abs pill" style="left:490px;top:246px;width:65px;height:22px;line-height:20px;background:var(--button-green);color:#fff;border-color:#6aa321">Available</div>
<div class="abs pill" style="left:559px;top:246px;width:79px;height:22px;line-height:20px;color:#999">Unavailable</div>

<div class="abs rule" style="left:364px;top:294px;width:358px"></div>
<div class="abs pill" style="left:620px;top:283px;width:43px;height:22px"><svg class="abs" style="left:9px;top:5px" width="24" height="12" viewBox="0 0 24 12"><rect x="0" y="0" width="12" height="9" fill="#666"/><path d="M17 8l3-4 3 4z" fill="#666"/></svg></div>
<div class="abs pill" style="left:667px;top:283px;width:45px;height:22px"><svg class="abs" style="left:10px;top:5px" width="24" height="12" viewBox="0 0 24 12"><rect x="0" y="0" width="11" height="11" fill="#666"/><path d="M16 4l3 4 3-4z" fill="#666"/></svg></div>

<div class="abs photo" role="img" aria-label="Photo of Mr. Ashcombe" style="left:401px;top:313px;width:35px;height:38px"></div>
<div class="abs name" style="left:449px;top:314px">Mr. Ashcombe</div>
<div class="abs small" style="left:449px;top:328px;width:222px;color:var(--muted)">Don't be late minibus will be leaving at 11:30 AM on the dot, anybody late will miss it!</div>
<div class="abs time" style="left:660px;top:343px;width:53px">2m ago</div>

<div class="abs photo" role="img" aria-label="Photo of Leah Varga" style="left:401px;top:373px;width:35px;height:38px"></div>
<div class="abs name" style="left:449px;top:373px">Leah Varga</div>
<div class="abs small" style="left:449px;top:387px;width:225px;color:var(--muted)">Remember last time we played this lot, thay had that really good center forward, whoever is marking him, stay tight to him</div>
<div class="abs time" style="left:660px;top:418px;width:53px">1h ago</div>

<div class="abs photo" role="img" aria-label="Photo of Nina Holt" style="left:401px;top:448px;width:35px;height:38px"></div>
<div class="abs name" style="left:449px;top:448px">Nina Holt</div>
<div class="abs small" style="left:449px;top:462px;width:220px;color:var(--muted)">Yeah and also quick passes as this lot will close you down really quick</div>
<div class="abs time" style="left:660px;top:477px;width:53px">6h ago</div>

<div class="abs" style="left:449px;top:512px;width:186px;height:24px;border:1px solid #c8ccc2;background:rgba(255,255,255,0.6);font-size:10px;color:#bbb;padding:5px 8px">Leave your comment here</div>
<div class="abs pill" style="left:641px;top:512px;width:70px;height:24px;line-height:22px;font-weight:700">Submit</div>

<div class="abs label" style="left:364px;top:575px;font-size:11px">LAST RESULT</div>
<div class="abs icon-box" style="left:365px;top:608px"><svg width="22" height="22" viewBox="0 0 22 22"><circle cx="11" cy="11" r="10" fill="#fff" stroke="#333" stroke-width="1.5"/><path d="M11 6l4 3-1.5 4.5h-5L7 9z" fill="#333"/></svg></div>
<div class="abs mini" style="left:414px;top:616px"><svg width="12" height="12" viewBox="0 0 12 12"><path d="M1 11V5h3v6M4.5 11V2h3v9M8 11V6h3v5" fill="none" stroke="#777"/></svg></div>
<div class="abs small" style="left:449px;top:612px"><span class="green">Ashford Dales</span> vs <span class="red">Kingsmere U15</span></div>
<div class="abs small" style="left:449px;top:627px;color:#666">Friday, 27th July, 1 PM</div>
<div class="abs pill" style="left:450px;top:651px;width:25px;height:25px;border-radius:2px;line-height:23px;font-size:14px;font-weight:700">2</div>
<div class="abs" style="left:482px;top:653px;font-size:14px;font-weight:700;color:#555">:</div>
<div class="abs pill" style="left:495px;top:651px;width:25px;height:25px;border-radius:2px;line-height:23px;font-size:14px;font-weight:700">1</div>

<div class="abs rule" style="left:364px;top:704px;width:358px"></div>
<div class="abs pill" style="left:630px;top:693px;width:33px;height:22px"><svg class="abs" style="left:10px;top:5px" width="12" height="11"><rect width="12" height="9" fill="#aaa"/></svg></div>
<div class="abs pill" style="left:667px;top:693px;width:45px;height:22px"><svg class="abs" style="left:10px;top:5px" width="24" height="12" viewBox="0 0 24 12"><rect x="0" y="0" width="11" height="11" fill="#666"/><path d="M16 4l3 4 3-4z" fill="#666"/></svg></div>

<div class="abs label" style="left:364px;top:735px;font-size:11px">NEWS FEED</div>
<div class="abs" style="left:425px;top:790px;width:1px;height:190px;background:#c8ccc2"></div>

<div class="abs photo" role="img" aria-label="Photo of Mr. Ashcombe" style="left:365px;top:767px;width:35px;height:38px"></div>
<div class="abs mini" style="left:414px;top:770px"><svg width="12" height="12" viewBox="0 0 12 12"><path d="M1 11V5h3v6M4.5 11V2h3v9M8 11V6h3v5" fill="none" stroke="#777"/></svg></div>
<div class="abs small" style="left:449px;top:772px"><span class="name">Mr. Ashcombe</span> invites you to a match</div>
<div class="abs small" style="left:449px;top:787px"><span class="green">U15 Football Team</span> vs <span class="red">Colossians House</span></div>
<div class="abs small" style="left:449px;top:802px;color:#666">Sunday, 29th July, 1 PM</div>
<svg class="abs" style="left:697px;top:778px" width="13" height="13" viewBox="0 0 13 13"><rect x="0.5" y="1.5" width="12" height="11" fill="none" stroke="#555"/><path d="M0 4.5h13M3 7h7M3 9.5h7" stroke="#555"/></svg>
<div class="abs" style="left:449px;top:831px;font-size:10px;font-weight:700;color:#444">RSVP:</div>
<svg class="abs" style="left:489px;top:823px" width="26" height="26" viewBox="0 0 26 26"><circle cx="13" cy="13" r="12" fill="var(--button-green)"/><path d="M7 13l4 4 8-8" fill="none" stroke="#fff" stroke-width="2.4"/></svg>
<svg class="abs" style="left:519px;top:825px" width="22" height="22" viewBox="0 0 22 22"><circle cx="11" cy="11" r="10" fill="#eee" stroke="#c4c4c4"/><path d="M7.5 7.5l7 7M14.5 7.5l-7 7" stroke="#888" stroke-width="2"/></svg>
<div class="abs time" style="left:660px;top:830px;width:53px">1h ago</div>

<div class="abs photo" role="img" aria-label="Photo of Nina Holt" style="left:365px;top:875px;width:35px;height:38px"></div>
<div class="abs mini" style="left:414px;top:884px"><svg width="12" height="12" viewBox="0 0 12 12"><path d="M6 1c1 3 4 4 4 7a4 4 0 0 1-8 0c0-2 1-3 2-4 0 1 .5 2 1.5 2C5 4 5 2.5 6 1z" fill="#777"/></svg></div>
<div class="abs small" style="left:449px;top:874px"><span class="name">Nina Holt</span> has challenged you to <b>squash</b></div>
<div class="abs small" style="left:449px;top:893px;color:#666">Sunday, 1st August, 1 PM. Linden Sports Centre</div>
<div class="abs" style="left:449px;top:923px;font-size:10px;font-weight:700;color:#444">RSVP:</div>
<svg class="abs" style="left:490px;top:917px" width="22" height="22" viewBox="0 0 22 22"><circle cx="11" cy="11" r="10" fill="#eee" stroke="#c4c4c4"/><path d="M6 11l3.5 3.5 6.5-7" fill="none" stroke="#888" stroke-width="2"/></svg>
<svg class="abs" style="left:519px;top:917px" width="22" height="22" viewBox="0 0 22 22"><circle cx="11" cy="11" r="10" fill="#eee" stroke="#c4c4c4"/><path d="M7.5 7.5l7 7M14.5 7.5l-7 7" stroke="#888" stroke-width="2"/></svg>
<div class="abs time" style="left:660px;top:922px;width:53px">6h ago</div>

<div class="abs photo" role="img" aria-label="Photo of Peter Ennis" style="left:365px;top:968px;width:35px;height:38px"></div>
<div class="abs mini" style="left:414px;top:977px"><svg width="12" height="12" viewBox="0 0 12 12"><path d="M3 1h6v3a3 3 0 0 1-6 0zM6 7v3M3.5 11h5" fill="none" stroke="#777" stroke-width="1.3"/></svg></div>
<div class="abs small" style="left:449px;top:973px"><span class="name">Peter Ennis</span> gained an achievement</div>
<div class="abs small" style="left:449px;top:988px;font-weight:700;color:#444">“Played 100 hours of sport”</div>
<div class="abs time" style="left:660px;top:989px;width:53px">2d ago</div>

<!-- Right column -->
<aside class="abs panel" style="left:746px;top:154px;width:287px;height:977px"></aside>

<div class="abs label faded" style="left:778px;top:173px;font-size:13px">UPCOMING FIXTURES</div>
<div class="abs hatch" style="left:930px;top:180px;width:68px"></div>
<div class="abs" style="left:791px;top:236px;width:1px;height:160px;background:#c8ccc2"></div>

<div class="abs mini" style="left:779px;top:220px;border-radius:4px;width:24px"><svg width="14" height="12" viewBox="0 0 12 12"><path d="M1 11V5h3v6M4.5 11V2h3v9M8 11V6h3v5" fill="none" stroke="#777"/></svg></div>
<svg class="abs" style="left:780px;top:256px" width="22" height="22" viewBox="0 0 22 22"><circle cx="11" cy="11" r="10" fill="#fff" stroke="#333" stroke-width="1.5"/><path d="M11 6l4 3-1.5 4.5h-5L7 9z" fill="#333"/></svg>
<div class="abs" style="left:824px;top:214px;font-size:13px;line-height:18px;width:180px"><span class="green">U15 Football Team</span> vs <span class="red">Colossians House</span></div>
<div class="abs" style="left:824px;top:251px;font-size:12px;font-weight:700;color:#555">29th July</div>
<div class="abs" style="left:824px;top:278px;font-size:12px;font-weight:700;color:#555">RSVP:&nbsp; Available</div>

<div class="abs rule" style="left:748px;top:320px;width:282px"></div>

<div class="abs mini" style="left:779px;top:354px;border-radius:4px;width:24px"><svg width="14" height="12" viewBox="0 0 12 12"><path d="M1 11V5h3v6M4.5 11V2h3v9M8 11V6h3v5" fill="none" stroke="#777"/></svg></div>
<svg class="abs" style="left:780px;top:391px" width="22" height="22" viewBox="0 0 22 22"><circle cx="11" cy="11" r="10" fill="#fff" stroke="#333" stroke-width="1.5"/><path d="M11 6l4 3-1.5 4.5h-5L7 9z" fill="#333"/></svg>
<div class="abs" style="left:824px;top:347px;font-size:13px;line-height:18px;width:180px"><span class="green">U15 Football Team</span> vs <span class="red">Romans House</span></div>
<div class="abs" style="left:824px;top:383px;font-size:12px;font-weight:700;color:#555">6th August</div>
<div class="abs" style="left:824px;top:412px;font-size:12px;font-weight:700;color:#555">RSVP:&nbsp; Available</div>

<div class="abs label faded" style="left:778px;top:479px;font-size:13px">LEAGUE TABLE</div>
<section class="abs card league-table">
  <div class="abs" style="left:20px;top:16px;font-size:11px;font-weight:700;color:#555">Ashford Inter House Football</div>
  <div class="abs rule" style="left:0;top:45px;width:246px"></div>
</section>
<div class="abs league-row" style="top:594px"><span class="pos">1</span><span class="team">Colossians</span><span class="played">12</span><span class="pts">36</span></div>
<div class="abs league-row" style="top:631px"><span class="pos">2</span><span class="team">Philippians</span><span class="played">12</span><span class="pts">30</span></div>
<div class="abs pill" style="left:814px;top:664px;width:76px;height:22px"></div>
<div class="abs league-row" style="top:668px"><span class="pos">3</span><span class="team">Galatians</span><span class="played">11</span><span class="pts">12</span></div>
<div class="abs league-row" style="top:706px"><span class="pos">4</span><span class="team">Romans</span><span class="played">12</span><span class="pts">4</span></div>
<div class="abs league-row" style="top:743px"><span class="pos">5</span><span class="team">Corinthians</span><span class="played">11</span><span class="pts">1</span></div>

<footer class="abs bottom-bar"></footer>

</body>
</html>
```